Brochure for 2015 workshops

Looking for a brochure for Skip Along Blue Kite ,2015 professional development workshops. We are a creative consulting company for early childhood and looking at getting the brochure designed in a fun, recyclable and quirky design.I have attached all information needed to be included into the brochure as well as our logo.

Industry/Entity Type

It Company

```html
<!DOCTYPE html>
<html lang="en">
<head>
<meta charset="utf-8">
<title>Skip Along Blue Kite – Professional Development Workshops 2015</title>
<link rel="stylesheet" href="https://fonts.googleapis.com/css2?family=Archivo+Black&family=Comic+Neue:wght@700&family=Lato:wght@400&display=swap">
<style>
  :root {
    --bg: #d9d9d9;
    --green: #5cab0f;
    --green-light: #8cc912;
    --yellow: #ffec00;
    --yellow-deep: #f2d600;
    --blue: #1496ec;
    --blue-deep: #0f7fd6;
    --orange: #e85a0c;
    --orange-light: #f06a12;
    --pink: #ec1a8c;
    --white: #ffffff;
    --ink: #111111;
    --cocoa: #4a2a10;
  }
  * { margin: 0; padding: 0; box-sizing: border-box; }
  html, body { width: 1200px; height: 900px; overflow: hidden; background: var(--bg); }
  .brochure {
    position: absolute; left: 116px; top: 98px; width: 984px; height: 700px;
    font-family: "Comic Neue", "Comic Sans MS", cursive;
    font-weight: 700;
  }
  .panels { position: absolute; inset: 0; }
  .abs { position: absolute; }
  .center { text-align: center; }

  /* left panel */
  .price { left: 0; width: 338px; top: 30px; font-size: 58px; color: var(--yellow); line-height: 1; }
  .per-person { left: 0; width: 338px; top: 94px; font-size: 45px; color: var(--white); line-height: 1; }
  .max-people { left: 0; width: 338px; top: 142px; font-size: 31px; color: var(--ink); line-height: 1; }
  .workshop-tag {
    left: 0; top: 262px; width: 148px; height: 33px; padding-left: 22px;
    background: var(--blue); color: var(--white); font-size: 18px; line-height: 33px;
    border-radius: 0 17px 17px 0;
  }
  .workshop-copy {
    left: 22px; top: 322px; width: 276px;
    font-family: "Lato", Arial, sans-serif; font-weight: 400;
    font-size: 13.2px; line-height: 17px; color: var(--ink);
  }
  .morning-tea {
    left: 149px; top: 610px; width: 189px; height: 60px; padding-top: 5px;
    background: var(--orange-light); border-radius: 30px 0 0 30px;
    font-size: 21px; line-height: 25px;
  }
  .morning-tea .tea-line { display: block; color: var(--ink); padding-left: 28px; }
  .morning-tea .tea-provided { display: block; color: var(--white); text-align: right; padding-right: 10px; }

  /* middle panel */
  .session-card {
    left: 321px; top: 172px; width: 270px; height: 272px;
    background: linear-gradient(160deg, var(--orange-light), var(--orange));
    border-radius: 12px; box-shadow: 0 8px 14px rgba(0,0,0,0.25);
    text-align: center; padding-top: 28px;
  }
  .session-card .label { font-size: 31px; color: var(--white); line-height: 1; }
  .session-card .presenter { font-size: 24px; color: var(--ink); line-height: 1.2; }
  .session-card .day { font-size: 27px; color: var(--yellow); line-height: 1.1; margin-top: 2px; }
  .session-card .date { font-size: 17px; color: var(--yellow); line-height: 1; }
  .session-card .time { font-size: 30px; color: var(--ink); margin-top: 8px; line-height: 1; }
  .session-card .duration { font-size: 28px; color: var(--yellow); margin-top: 14px; line-height: 1; }
  .session-card .hours { font-size: 35px; color: var(--white); line-height: 1.05; }

  .venue-title { left: 336px; width: 326px; top: 482px; font-size: 25px; color: var(--yellow); }
  .venue-address { left: 336px; width: 326px; top: 517px; font-size: 15px; line-height: 18px; color: var(--white); }
  .call-title { left: 336px; width: 326px; top: 568px; font-size: 34px; color: var(--yellow); }
  .call-phone { left: 336px; width: 326px; top: 610px; font-size: 28px; color: var(--white); }
  .call-email { left: 336px; width: 326px; top: 652px; font-size: 15px; color: var(--white); }

  /* right panel */
  .headline {
    left: 660px; width: 324px; top: 52px;
    font-family: "Archivo Black", "Arial Black", sans-serif; font-weight: 400;
    font-size: 44px; line-height: 38px; letter-spacing: -3px; color: var(--pink);
  }
  .headline .brand-name { color: var(--white); display: block; font-size: 42px; line-height: 40px; margin-top: 2px; }
  .crayon-art {
    left: 740px; top: 268px; width: 220px; height: 110px;
    background: radial-gradient(ellipse at 50% 50%, rgba(30,110,220,0.22), rgba(255,236,0,0) 70%);
    border-radius: 50%;
  }
  .brand-art {
    left: 722px; top: 458px; width: 190px; height: 120px;
    background: linear-gradient(135deg, rgba(90,50,20,0.35), rgba(90,50,20,0.15));
    border-radius: 16px;
  }
  .brand-lockup {
    left: 660px; width: 324px; top: 583px;
    font-size: 19px; color: var(--cocoa);
    display: flex; align-items: center; justify-content: center; gap: 8px;
  }
  .brand-lockup .dot { width: 12px; height: 12px; border-radius: 50%; background: var(--cocoa); }
  .series-badge {
    left: 674px; top: 619px; width: 296px; height: 61px; padding-top: 7px;
    background: var(--orange-light); border-radius: 30px;
    font-size: 18px; line-height: 24px; color: var(--white);
  }
  .series-badge .year { display: block; font-size: 21px; color: var(--yellow); }
</style>
</head>
<body>
<main class="brochure">
  <svg class="panels" width="984" height="700" viewBox="0 0 984 700" aria-hidden="true">
    <defs>
      <linearGradient id="left-yellow" x1="0" y1="0" x2="1" y2="0">
        <stop offset="0" stop-color="#fff200"/><stop offset="1" stop-color="#e8cf00"/>
      </linearGradient>
      <linearGradient id="left-green" x1="0" y1="0" x2="1" y2="0">
        <stop offset="0" stop-color="#8cc912"/><stop offset="1" stop-color="#3f9410"/>
      </linearGradient>
      <linearGradient id="mid-blue" x1="0" y1="0" x2="1" y2="0">
        <stop offset="0" stop-color="#0f86e0"/><stop offset="1" stop-color="#16a0f2"/>
      </linearGradient>
    </defs>
    <rect x="0" y="0" width="336" height="700" fill="url(#left-yellow)"/>
    <path d="M0 0 H336 V258 C160 175 60 190 0 240 Z" fill="url(#left-green)"/>
    <path d="M0 240 C60 190 160 175 336 258" fill="none" stroke="#1a7fd8" stroke-width="12"/>
    <rect x="336" y="0" width="324" height="700" fill="url(#mid-blue)"/>
    <rect x="660" y="0" width="324" height="700" fill="#ffec00"/>
    <path d="M660 410 C760 460 870 440 984 370 V700 H660 Z" fill="#7cbf12"/>
    <path d="M660 410 C760 460 870 440 984 370" fill="none" stroke="#1a7fd8" stroke-width="8"/>
  </svg>

  <section class="panel-pricing">
    <div class="abs price center">$60</div>
    <div class="abs per-person center">PER PERSON</div>
    <div class="abs max-people center">(MAX: 20 PEOPLE)</div>
    <div class="abs workshop-tag">Little Diggers</div>
    <div class="abs workshop-copy">
      <p>Creative play in the humble sandpit has never been so interesting! So much more than a place to build</p>
      <p>castles, the sandpit presents an exciting opportunity for early childhood workers to unleash the teacher within!</p>
      <p>There is no right way or wrong way to use sand…except maybe throwing it! Sandpits invite participation.</p>
      <p>Children’s ideas are made and tested, their imaginations are stretched and they can be soothed by the sensory experience of digging in deep.</p>
      <p>So much sand, so much can be done, so much is to be gained from doing it!</p>
    </div>
    <div class="abs morning-tea"><span class="tea-line">Morning Tea</span><span class="tea-provided">provided</span></div>
  </section>

  <section class="panel-details">
    <div class="abs session-card">
      <div class="label">PRESENTER</div>
      <div class="presenter">DANA WHITMORE</div>
      <div class="day">WEDNESDAY</div>
      <div class="date">11TH MARCH 2015</div>
      <div class="time">9.30-12.30</div>
      <div class="duration">DURATION:</div>
      <div class="hours">3 HOURS</div>
    </div>
    <div class="abs venue-title center">Venue</div>
    <div class="abs venue-address center">Maple Grove Community Hall,<br>28 Wattle St, Elmwood North</div>
    <div class="abs call-title center">Call Today</div>
    <div class="abs call-phone center">0400 218 764</div>
    <div class="abs call-email center">mia.hartley@skipalongbluekite.com.au</div>
  </section>

  <section class="panel-cover">
    <div class="abs crayon-art" role="img" aria-label="Blue crayon drawing a smiling face"></div>
    <h1 class="abs headline center">MEET<br>THE PEOPLE<br>BEHIND<span class="brand-name">SKIP ALONG<br>BLUE KITE</span></h1>
    <div class="abs brand-art" role="img" aria-label="Playful illustration area for the company mascot"></div>
    <div class="abs brand-lockup"><span class="dot"></span>Skip Along Blue Kite</div>
    <div class="abs series-badge center">PROFESSIONAL DEVELOPMENT<span class="year">WORKSHOPS FOR 2015</span></div>
  </section>
</main>
</body>
</html>
```